Creation of a cover for a novel on immigration in Paris, with one of the two joined images. These photos can be modified (shape, colors…)
Size: 14 x 20.5 cm (vertical) with 5 mm bleed on the top, bottom and right areas.

TITLE: "Teodor, the Wanderer" (and not "African immigrant in Paris)
AUTHOR: “Lucien Marvaud”
NOTICES TO BE ADDED:
- “Novel” (witch means novel)
- “Preface by Solenne Varek” (the preface writer)
PUBLISH “Editions Pluvane” (AT THE BOTTOM OF THE PAGE)

Target Market(s)

Book shops

Industry/Entity Type

Book cover

Requirements
Must have
• One of the two images joined

```html
<!DOCTYPE html>
<html lang="en">
<head>
<meta charset="utf-8">
<title>Teodor, the Wanderer — Book Cover</title>
<link rel="stylesheet" href="https://fonts.googleapis.com/css2?family=Ultra&family=Montserrat:wght@400;600&family=Open+Sans:wght@300&display=swap">
<style>
  :root {
    --ink: #000000;
    --paper: #ffffff;
    --title-white: #e6e6e6;
    --accent-yellow: #f6b300;
    --text-grey: #e8e8e8;
    --haze: #5a5a5a;
  }
  html, body {
    margin: 0;
    padding: 0;
    width: 1200px;
    height: 821px;
    overflow: hidden;
    background: var(--ink);
  }
  .cover {
    position: relative;
    width: 1200px;
    height: 821px;
    overflow: hidden;
    background:
      radial-gradient(ellipse 260px 520px at 250px 300px, rgba(110,110,110,0.45), transparent 70%),
      radial-gradient(ellipse 380px 220px at 300px 560px, rgba(90,90,90,0.35), transparent 70%),
      radial-gradient(ellipse 200px 300px at 520px 620px, rgba(70,70,70,0.3), transparent 70%),
      var(--ink);
    color: var(--paper);
  }

  /* Front panel photograph area */
  .front-photo {
    position: absolute;
    left: 640px;
    top: 0;
    width: 560px;
    height: 821px;
    background:
      radial-gradient(ellipse 120px 330px at 390px 420px, rgba(150,150,150,0.55), transparent 75%),
      radial-gradient(ellipse 320px 70px at 330px 600px, rgba(210,210,210,0.45), transparent 75%),
      linear-gradient(180deg, #050505 0%, #111 35%, #2a2a2a 70%, #3c3c3c 85%, #151515 100%);
    -webkit-mask-image: linear-gradient(90deg, transparent 0%, #000 18%);
    mask-image: linear-gradient(90deg, transparent 0%, #000 18%);
  }

  /* Back cover */
  .back-title {
    position: absolute;
    left: 74px;
    top: 176px;
    margin: 0;
    font-family: "Ultra", serif;
    font-weight: 400;
    line-height: 1;
  }
  .back-title .name {
    display: block;
    font-size: 44px;
    color: var(--title-white);
    letter-spacing: 1px;
  }
  .back-title .epithet {
    display: block;
    margin: 4px 0 0 12px;
    font-size: 22px;
    color: var(--accent-yellow);
    letter-spacing: 1px;
  }
  .blurb {
    position: absolute;
    left: 75px;
    top: 272px;
    width: 430px;
    font-family: "Montserrat", sans-serif;
    font-size: 13.4px;
    line-height: 23.4px;
    color: var(--text-grey);
  }
  .blurb p { margin: 0 0 23.4px; }
  .blurb strong { font-weight: 600; color: var(--paper); }
  .publisher-block {
    position: absolute;
    left: 78px;
    top: 715px;
    display: flex;
    align-items: flex-end;
    gap: 23px;
  }
  .publisher-block .mark {
    width: 102px;
    height: 78px;
    background: var(--paper);
  }
  .publisher-block .imprint {
    font-family: "Open Sans", sans-serif;
    font-weight: 300;
    font-size: 26px;
    line-height: 1;
    padding-bottom: 6px;
  }

  /* Spine */
  .spine-title {
    position: absolute;
    left: 586px;
    top: 118px;
    writing-mode: vertical-rl;
    font-family: "Ultra", serif;
    font-size: 21px;
    line-height: 1;
    letter-spacing: 1px;
    white-space: nowrap;
  }
  .spine-title .name { color: var(--title-white); }
  .spine-title .epithet { color: var(--accent-yellow); margin-top: 10px; }
  .spine-author {
    position: absolute;
    left: 592px;
    top: 510px;
    writing-mode: vertical-rl;
    font-family: "Montserrat", sans-serif;
    font-weight: 600;
    font-size: 12px;
    letter-spacing: 7.6px;
    color: var(--paper);
    white-space: nowrap;
  }

  /* Front cover */
  .front-imprint {
    position: absolute;
    left: 640px;
    width: 540px;
    top: 34px;
    text-align: center;
    font-family: "Open Sans", sans-serif;
    font-weight: 300;
    font-size: 25px;
  }
  .front-title {
    position: absolute;
    left: 680px;
    width: 460px;
    top: 140px;
    margin: 0;
    text-align: center;
    font-family: "Ultra", serif;
    font-weight: 400;
    line-height: 1;
  }
  .front-title .name {
    display: block;
    font-size: 78px;
    color: var(--title-white);
    letter-spacing: 1px;
  }
  .front-title .epithet {
    display: block;
    margin-top: 16px;
    font-size: 38px;
    color: var(--accent-yellow);
    letter-spacing: 1px;
  }
  .genre {
    position: absolute;
    left: 640px;
    width: 544px;
    top: 301px;
    text-align: center;
    font-family: "Montserrat", sans-serif;
    font-size: 24px;
    letter-spacing: 17px;
    padding-left: 17px;
    box-sizing: border-box;
  }
  .front-author {
    position: absolute;
    left: 640px;
    width: 544px;
    top: 766px;
    text-align: center;
    font-family: "Montserrat", sans-serif;
    font-size: 27px;
    letter-spacing: 15px;
    white-space: nowrap;
  }
</style>
</head>
<body>
<main class="cover">
  <div class="front-photo" role="img" aria-label="Black and white night photograph: a man with a backpack and bag, seen from behind, walking along the Seine bank with the lit Eiffel Tower and a bridge reflected in the water"></div>

  <section class="back-cover">
    <h2 class="back-title">
      <span class="name">TEODOR</span>
      <span class="epithet">THE WANDERER</span>
    </h2>
    <div class="blurb">
      <p><strong>Filler text</strong> (also placeholder text or dummy text) is text that shares some characteristics of a real written text, but is random or otherwise generated. It may be used to display a sample of fonts, generate text for testing, or to spoof an e-mail spam filter. The process of using filler text is sometimes called greeking, although the text itself may be nonsense, or largely Latin, as in Lorem ipsum.</p>
      <p>ASDF is the sequence of letters that appear on the first four keys on the home row of a QWERTY or QWERTZ keyboard. They are often used as a sample or test case or as random, meaningless nonsense. It is also a common learning tool for keyboard classes, since all four keys are located on Home row.</p>
    </div>
    <div class="publisher-block">
      <div class="mark"></div>
      <span class="imprint">Editions Pluvane</span>
    </div>
  </section>

  <section class="spine">
    <div class="spine-title"><span class="name">TEODOR</span><span class="epithet">THE WANDERER</span></div>
    <div class="spine-author">Lucien Marvaud</div>
  </section>

  <section class="front-cover">
    <div class="front-imprint">Editions Pluvane</div>
    <h1 class="front-title">
      <span class="name">TEODOR</span>
      <span class="epithet">THE WANDERER</span>
    </h1>
    <div class="genre">Novel</div>
    <div class="front-author">Lucien Marvaud</div>
  </section>
</main>
</body>
</html>
```